Infectious Diseases Research Laboratory Needs Business Card

We need a business card for an academic research laboratory based in Kansas City called MORVEK. The full lab name is Microbial Dose-Response/Exposure Bridging Studies Laboratory, but this does not need to be incorporated. We study novel ways to optimize the treatment of multidrug-resistant bacterial infections ("superbugs") throughout the entire biomedical research spectrum (from benchtop to bedside). The name MORVEK is not only an acronym for our lab name, but also represents our desire to make discoveries and explore the unknown (the stars, if you well). It also serves as an ode to the state of Kansas motto where we are based, ad astra per aspera ("to the stars, through difficulty").

Target Market(s)

Pharmaceutical companies, researchers

Industry/Entity Type

Pharmaceutical

Contact Information for Business Card

The business card should incorporate and complement our new logo (see uploaded files). Double-sided designs are preferred. Looking for something modern, but professional.

Font styles to use
Sans Serif

Requirements
Must have
• Double-sided. One side would ideally be a solid color incorporating logo and the other should also have the logo (smaller), but incorporate staff information.
• Color codes:
• Red: #F04C51
• Blue: #3477B5
• Gray: #808285

```html
<!DOCTYPE html>
<html lang="en">
<head>
<meta charset="utf-8">
<title>MORVEK Business Card</title>
<link href="https://fonts.googleapis.com/css2?family=Open+Sans:wght@400;600;700&display=swap" rel="stylesheet">
<style>
  :root {
    --red: #F04C51;
    --blue: #3477B5;
    --blue-deep: #2a66a3;
    --gray: #808285;
    --ink: #4a4b4d;
    --paper: #f7f7f7;
    --backdrop: #5c5e60;
  }
  html, body {
    margin: 0;
    padding: 0;
    width: 1200px;
    height: 904px;
    overflow: hidden;
    background: var(--backdrop);
    font-family: "Open Sans", Arial, sans-serif;
  }
  .stage {
    position: relative;
    width: 1200px;
    height: 904px;
  }
  .card {
    position: absolute;
    width: 620px;
    height: 354px;
    box-shadow: 0 10px 24px rgba(0,0,0,0.35);
    box-sizing: border-box;
  }
  /* Front: solid brand colour */
  .card-front {
    left: 90px;
    top: 80px;
    background: radial-gradient(ellipse at 80% 20%, #4a8ac4 0%, var(--blue) 45%, var(--blue-deep) 100%);
    display: flex;
    align-items: center;
    justify-content: center;
  }
  .front-wordmark {
    color: #ffffff;
    font-weight: 600;
    font-size: 58px;
    letter-spacing: 6px;
    margin: 0;
  }
  /* Back: staff information */
  .card-back {
    left: 490px;
    top: 470px;
    background: linear-gradient(160deg, #ffffff 0%, var(--paper) 60%, #ececec 100%);
  }
  .back-logo {
    position: absolute;
    top: 38px;
    right: 48px;
    display: flex;
    align-items: center;
    gap: 14px;
  }
  .logo-dot {
    width: 34px;
    height: 34px;
    border-radius: 50%;
    background: var(--blue);
  }
  .logo-name {
    color: var(--red);
    font-weight: 600;
    font-size: 40px;
    letter-spacing: 4px;
  }
  .divider-top {
    position: absolute;
    top: 130px;
    left: 200px;
    right: 24px;
    height: 1px;
    background: #333;
  }
  .staff {
    position: absolute;
    left: 40px;
    bottom: 40px;
    width: 290px;
  }
  .staff-name {
    margin: 0;
    color: var(--blue);
    font-weight: 700;
    font-size: 21px;
    line-height: 1.1;
  }
  .staff-role {
    margin: 2px 0 8px;
    color: var(--ink);
    font-size: 14px;
  }
  .staff-rule {
    height: 1px;
    background: #333;
    margin-bottom: 8px;
  }
  .staff-address {
    margin: 0;
    color: var(--ink);
    font-size: 14px;
    line-height: 1.4;
    font-style: normal;
  }
  .contact {
    position: absolute;
    left: 350px;
    bottom: 52px;
    margin: 0;
    padding: 0;
    list-style: none;
  }
  .contact li {
    display: flex;
    align-items: center;
    gap: 10px;
    color: var(--ink);
    font-size: 14px;
    line-height: 22px;
  }
  .contact svg {
    width: 13px;
    height: 13px;
    fill: var(--red);
    flex: none;
  }
</style>
</head>
<body>
<main class="stage">
  <section class="card card-front" aria-label="Card front">
    <h1 class="front-wordmark">MORVEK</h1>
  </section>

  <section class="card card-back" aria-label="Card back">
    <div class="back-logo">
      <span class="logo-dot"></span>
      <span class="logo-name">MORVEK</span>
    </div>
    <div class="divider-top"></div>

    <div class="staff">
      <h2 class="staff-name">Dana Whitfield</h2>
      <p class="staff-role">Manager</p>
      <div class="staff-rule"></div>
      <address class="staff-address">2410 Holmes Street, Suite 5<br>Kansas City, MO 64108.</address>
    </div>

    <ul class="contact">
      <li>
        <svg viewBox="0 0 16 16" aria-hidden="true"><path d="M3.6 1.2l2.2 2.6-1.3 1.6c.9 2 2.3 3.4 4.2 4.3l1.6-1.3 2.6 2.2-1.1 2.4C7 12.7 3.3 9 1.2 4.3z"/></svg>
        +1 816 555 0142
      </li>
      <li>
        <svg viewBox="0 0 16 16" aria-hidden="true"><path d="M1 3h14v10H1z M2.5 4.5 8 9l5.5-4.5" fill="var(--red)"/><path d="M2.5 4.5 8 9l5.5-4.5" fill="none" stroke="#fff" stroke-width="1.2"/></svg>
        lab@morveklab.org
      </li>
      <li>
        <svg viewBox="0 0 16 16" aria-hidden="true"><circle cx="8" cy="8" r="7"/><path d="M1 8h14M8 1c-3 3.5-3 10.5 0 14M8 1c3 3.5 3 10.5 0 14" fill="none" stroke="#fff" stroke-width="1"/></svg>
        www.morveklab.org
      </li>
    </ul>
  </section>
</main>
</body>
</html>
```